New Web Design Project

Require a website for The Marrow Orchard. All relevant information is in the uploaded files.

website to be responsive to work on mobile.

Required in html5, css

Coding

Coded - Design and coding required

Number of Pages Required

3 page

```html
<!DOCTYPE html>
<html lang="en">
<head>
<meta charset="utf-8">
<title>The Marrow Orchard Company</title>
<link href="https://fonts.googleapis.com/css2?family=Poppins:wght@400;500;600;700;800&display=swap" rel="stylesheet">
<style>
:root{
  --ink:#2f3b44;
  --white:#ffffff;
  --hero-a:#a9c8dd;
  --hero-b:#b3cfe0;
  --green:#22c55e;
  --green-text:#1f4f33;
  --blue:#12a0e0;
  --navy:#1e4e79;
  --link:#1b74b8;
  --orange:#f97316;
  --orange-dark:#c2410c;
  --footer:#7b2d12;
  --about-a:#eefcf2;
  --about-b:#defbe8;
  --team-a:#ecf7ff;
  --team-b:#dceffd;
  --contact-a:#fff5ea;
  --contact-b:#ffecd8;
  --field-border:#f3c99b;
}
*{margin:0;padding:0;box-sizing:border-box}
html,body{width:1200px;height:2468px;overflow:hidden}
body{font-family:'Poppins',sans-serif;color:var(--ink);position:relative;background:var(--white)}
.abs{position:absolute}

/* hero */
.hero{left:0;top:0;width:1200px;height:634px;overflow:hidden}
.hero-photo{position:absolute;inset:0;background:linear-gradient(180deg,var(--hero-a),var(--hero-b))}
.site-header{position:absolute;left:0;top:0;width:1200px;height:105px;background:rgba(190,214,230,.5)}
.social-top{position:absolute;left:100px;top:43px;display:flex;gap:15px}
.social-top span{width:18px;height:18px;background:#3b4650;border-radius:50%}
.social-top span.sq{border-radius:4px}
.brand{position:absolute;left:0;width:1200px;top:36px;text-align:center;font-weight:700;font-size:20px;color:#3b4650}
.brand i{display:inline-block;width:14px;height:14px;border-radius:50%;background:var(--orange);margin-right:6px;vertical-align:1px}
.main-nav{position:absolute;right:76px;top:40px;display:flex;gap:41px;font-weight:500;font-size:15.5px;color:#3b4650}
.hero-title{position:absolute;left:0;width:1200px;top:196px;text-align:center;color:var(--white);font-weight:800;font-size:75px;line-height:72px;letter-spacing:-2.8px}
.hero-sub{position:absolute;left:403px;top:384px;width:400px;color:var(--white);font-size:15px;line-height:23px}
.hero-btn{position:absolute;left:520px;top:456px;width:160px;height:44px;border-radius:22px;background:rgba(130,150,160,.55);color:rgba(255,255,255,.85);font-weight:600;font-size:14px;letter-spacing:1px;text-align:center;line-height:44px}

/* about */
.about{left:0;top:634px;width:1200px;height:651px;background:linear-gradient(160deg,var(--about-a),var(--about-b))}
.section-title{position:absolute;left:184px;font-weight:800;font-size:53px;letter-spacing:-.5px}
.about .section-title{top:105px;color:var(--green)}
.col{position:absolute;width:375px;font-size:15.3px;line-height:24.2px;color:var(--green-text)}
.col p+p{margin-top:24px}
.col-left{left:184px;top:238px}
.col-right{left:641px;top:238px}
.pill{position:absolute;height:43px;border-radius:22px;color:var(--white);font-weight:600;font-size:14px;letter-spacing:.8px;text-align:center;line-height:43px}
.about .pill{left:641px;top:462px;width:143px;background:var(--green)}

/* team */
.team{left:0;top:1285px;width:1200px;height:469px;background:linear-gradient(160deg,var(--team-a),var(--team-b))}
.team .section-title{top:84px;color:var(--blue)}
.card{position:absolute;top:214px;width:395px;height:155px;background:var(--white);border-radius:8px;overflow:hidden;box-shadow:0 8px 24px rgba(30,110,180,.12)}
.card-photo{position:absolute;left:0;top:0;width:155px;height:155px}
.card-name{position:absolute;left:185px;top:30px;font-size:22.5px;font-weight:500;color:var(--navy)}
.card-role{position:absolute;left:185px;top:68px;font-size:15px;color:var(--link)}
.card-link{position:absolute;left:185px;top:122px;font-size:10.5px;color:var(--link);text-decoration:underline;display:flex;align-items:center;gap:8px}
.card-link i{width:17px;height:17px;border-radius:3px;background:var(--link);display:inline-block}

/* contact */
.contact{left:0;top:1754px;width:1200px;height:646px;background:linear-gradient(160deg,var(--contact-a),var(--contact-b))}
.contact .section-title{top:112px;color:var(--orange)}
.field{position:absolute;left:184px;width:409px;background:var(--white);border:1px solid var(--field-border);border-radius:6px;font-size:15px;color:#b9a89a;padding:13px 13px}
.resize{position:absolute;right:8px;bottom:8px}
.contact .pill{left:184px;top:521px;width:88px;background:var(--orange)}
.divider{position:absolute;left:693px;top:247px;width:1px;height:259px;background:var(--orange-dark);opacity:.6}
.social-list{position:absolute;left:795px;top:284px;list-style:none}
.social-list li{display:flex;align-items:center;gap:15px;height:54px;font-size:16px;color:var(--orange-dark)}
.social-list i{display:inline-block;width:23px;height:23px;background:var(--orange-dark);border-radius:50%}
.social-list i.sq{border-radius:5px}

.footer{left:0;top:2400px;width:1200px;height:68px;background:var(--footer);color:#fde8d8;font-size:15.5px;text-align:center;line-height:68px}
</style>
</head>
<body>

<section class="abs hero">
  <div class="hero-photo" role="img" aria-label="Blurred photo of fresh produce slices, leafy greens and fruit pieces on a pale blue background"></div>
  <header class="site-header">
    <div class="social-top"><span></span><span></span><span class="sq"></span><span class="sq"></span></div>
    <div class="brand"><i></i>The Marrow Orchard</div>
    <nav class="main-nav"><span>About Us</span><span>Team</span><span>Contact</span></nav>
  </header>
  <h1 class="hero-title">Expand your reach in the<br>fresh produce market.</h1>
  <p class="hero-sub">We introduce new vendors to the Canadian market through a trusted and mutual business relation.</p>
  <div class="hero-btn">GET IN TOUCH!</div>
</section>

<section class="abs about">
  <h2 class="section-title">About Us</h2>
  <div class="col col-left">
    <p>The Marrow Orchard Company was incorporated with the objective of introducing new vendors to the Canadian market through a trusted and mutual business relation</p>
    <p>It was set up by Omar Haddani and Nick Pavlidis who have a combined experience of over 45 years in the fresh produce business. With Omar's expertise in global sourcing and Nick's vast connection and know how of the Canadian market, we have helped our existing partners grow and expand their reach in the Canadian fresh produce market.</p>
  </div>
  <div class="col col-right">
    <p>Our expertise and supply chain knowledge allow us to develop programs and introduce new products to the Canadian consumer, via retail and wholesale channels across Canada.</p>
    <p>Get in touch to discuss how we can add value to your business</p>
  </div>
  <div class="pill">CONTACT US</div>
</section>

<section class="abs team">
  <h2 class="section-title">Team</h2>
  <article class="card" style="left:185px">
    <div class="card-photo" role="img" aria-label="Portrait photo of Omar Haddani" style="background:linear-gradient(160deg,#b5a88e,#5a5246)"></div>
    <div class="card-name">Omar Haddani</div>
    <div class="card-role">Global Sourcing Expert</div>
    <div class="card-link"><i></i>Go to WorkLink Profile</div>
  </article>
  <article class="card" style="left:621px">
    <div class="card-photo" role="img" aria-label="Portrait photo of Nick Pavlidis" style="background:linear-gradient(160deg,#8e8880,#2e3138)"></div>
    <div class="card-name">Nick Pavlidis</div>
    <div class="card-role">Collaborative Partner</div>
    <div class="card-link"><i></i>Go to WorkLink Profile</div>
  </article>
</section>

<section class="abs contact">
  <h2 class="section-title">Contact Us</h2>
  <div class="field" style="top:247px;height:49px">Name</div>
  <div class="field" style="top:311px;height:49px">Email</div>
  <div class="field" style="top:374px;height:132px">Message
    <svg class="resize" width="10" height="10" viewBox="0 0 10 10"><path d="M9 2L2 9M9 6L6 9" stroke="#999" stroke-width="1"/></svg>
  </div>
  <div class="pill">SEND</div>
  <div class="divider"></div>
  <ul class="social-list">
    <li><i></i>Friendbook</li>
    <li><i></i>Chirper</li>
    <li><i class="sq"></i>WorkLink</li>
    <li><i class="sq"></i>Snapgram</li>
  </ul>
</section>

<footer class="abs footer">© 2020 Copyright The Marrow Orchard Company</footer>

</body>
</html>
```